Business Card For Kelmora Financial Consulting

Hi, I would like a business card designed. Bold, modern.
Please use the same design as the logo. I have also attached the website design to see the overall theme.
Wordmark Font
Color: Hex: #01AEF7

```html
<!DOCTYPE html>
<html lang="en">
<head>
<meta charset="utf-8">
<title>Kelmora Financial Consulting – Business Card</title>
<link href="https://fonts.googleapis.com/css2?family=Open+Sans:wght@300;400;700&display=swap" rel="stylesheet">
<style>
  :root {
    --backdrop: #232323;
    --card: #0b4468;
    --card-edge: #08385a;
    --accent: #01aef7;
    --ink: #ffffff;
    --ink-soft: #d6e4ef;
  }
  * { box-sizing: border-box; margin: 0; padding: 0; }
  html, body { width: 1200px; height: 780px; overflow: hidden; background: var(--backdrop); }
  body { position: relative; font-family: "Open Sans", Arial, sans-serif; color: var(--ink); }

  .card {
    position: absolute;
    width: 525px;
    height: 300px;
    background: var(--card);
    border-radius: 3px;
    box-shadow: 0 3px 0 var(--card-edge), 0 6px 0 #062f4c, 0 18px 30px rgba(0,0,0,.55);
    overflow: hidden;
  }
  .card--front { left: 70px; top: 90px; }
  .card--back { left: 605px; top: 390px; }

  .person { position: absolute; left: 36px; top: 32px; }
  .person__name { font-weight: 700; font-size: 24px; letter-spacing: .2px; }
  .person__role { font-weight: 300; font-size: 13px; color: var(--ink-soft); margin-top: 2px; }

  .brand { position: absolute; display: flex; align-items: center; gap: 10px; }
  .brand__mark { width: 12px; height: 12px; background: var(--accent); }
  .brand__name { font-weight: 700; font-size: 20px; letter-spacing: 2px; text-transform: uppercase; color: var(--ink); }
  .card--front .brand { right: 34px; top: 108px; }
  .card--back .brand { right: 40px; top: 134px; }
  .card--back .brand__name { font-size: 24px; }

  .address { position: absolute; right: 34px; top: 160px; text-align: right; font-size: 14px; line-height: 1.35; }

  .contacts { position: absolute; right: 30px; bottom: 20px; list-style: none; text-align: right; font-size: 14px; line-height: 1.45; }
  .contacts li { display: flex; justify-content: flex-end; align-items: center; gap: 8px; }
  .contacts svg { width: 13px; height: 13px; fill: none; stroke: var(--accent); stroke-width: 2; }
</style>
</head>
<body>
  <section class="card card--front" aria-label="Business card front">
    <div class="person">
      <p class="person__name">Lena Marovic</p>
      <p class="person__role">Managing Director</p>
    </div>
    <div class="brand">
      <span class="brand__mark"></span>
      <span class="brand__name">Kelmora Consulting</span>
    </div>
    <p class="address">1840 Linden Ave. Suite 300<br>Oak Ridge, TX 75210</p>
    <ul class="contacts">
      <li>(555) 214-6038
        <svg viewBox="0 0 16 16" aria-hidden="true"><path d="M4 2l2 3-1.5 1.5a8 8 0 0 0 5 5L11 10l3 2-1 2.5C7 14 2 9 1.5 3z"/></svg>
      </li>
      <li>info@kelmora.com
        <svg viewBox="0 0 16 16" aria-hidden="true"><rect x="1.5" y="3.5" width="13" height="9"/><path d="M1.5 3.5l6.5 5 6.5-5"/></svg>
      </li>
      <li>www.kelmora.com
        <svg viewBox="0 0 16 16" aria-hidden="true"><circle cx="8" cy="8" r="6.5"/><path d="M1.5 8h13M8 1.5c3 3.5 3 9.5 0 13M8 1.5c-3 3.5-3 9.5 0 13"/></svg>
      </li>
    </ul>
  </section>

  <section class="card card--back" aria-label="Business card back">
    <div class="brand">
      <span class="brand__mark"></span>
      <span class="brand__name">Kelmora Consulting</span>
    </div>
  </section>
</body>
</html>
```